A-Stand Directional Sign Design

Objective:
We need a professional graphic design for an A-Stand sign that will guide customers arriving in our parking lot to our office. The design should be visually clear, welcoming, and aligned with our brand identity.
REQUIREMENTS:
Two versions of the design:
- One with an arrow pointing left
- One with an arrow pointing right
(This allows us to place the A-Stand anywhere and flip the graphic as needed.)
DIMENSIONS:
- Viewable Area: 30" x 40"
BRAND ALIGNMENT:
- Colors, fonts, and overall style should match our website: www.skornabel.com
- Clean, modern, and professional look consistent with our aviation/tourism brand
CONTENT:
- Clear directional arrow (left or right depending on version)
- Text: “Office Entrance” or similar concise wording (designers may propose alternatives if they improve clarity)
READABILITY:
- Bold, high-contrast design for visibility from a distance
- Simple layout that avoids clutter
DELIVERABLES:
- Final artwork in print-ready format (PDF preferred)
- Two versions: Arrow Left and Arrow Right
DESIGN GOAL:
Ensure customers can easily find our office upon arrival, while reinforcing skorNABEL’s professional and welcoming brand image.
Target Market(s)
Tourism

```html
<!DOCTYPE html>
<html lang="en">
<head>
<meta charset="utf-8">
<title>skorNABEL A-Stand Directional Signs</title>
<link href="https://fonts.googleapis.com/css2?family=Oswald:wght@600;700&display=swap" rel="stylesheet">
<style>
  :root {
    --page-bg: #eeeeef;
    --brand-blue: #2452a8;
    --brand-blue-deep: #1c458f;
    --panel-line: #8fa9d8;
    --sign-white: #ffffff;
    --name-blue: #1e4b9e;
  }
  html, body {
    margin: 0;
    padding: 0;
    width: 1200px;
    height: 2560px;
    overflow: hidden;
    background: var(--page-bg);
  }
  .canvas {
    position: relative;
    width: 1200px;
    height: 2560px;
    display: flex;
    flex-direction: column;
    align-items: center;
    justify-content: space-around;
  }
  .sign-face {
    width: 840px;
    height: 1120px;
    background: var(--sign-white);
    box-sizing: border-box;
    padding: 18px;
    display: flex;
    flex-direction: column;
    box-shadow: 0 0 0 1px #dcdcdc;
  }
  .brand-header {
    height: 210px;
    display: flex;
    align-items: center;
    justify-content: center;
    gap: 22px;
  }
  .brand-mark {
    width: 54px;
    height: 54px;
    border-radius: 50%;
    background: var(--name-blue);
  }
  .brand-name {
    font-family: "Oswald", sans-serif;
    font-weight: 700;
    font-size: 88px;
    letter-spacing: 1px;
    color: var(--name-blue);
    line-height: 1;
  }
  .direction-panel {
    flex: 1;
    background: radial-gradient(ellipse at 60% 40%, var(--brand-blue) 0%, var(--brand-blue-deep) 100%);
    padding: 22px;
    box-sizing: border-box;
    display: flex;
  }
  .panel-frame {
    flex: 1;
    border: 3px solid var(--panel-line);
    display: flex;
    flex-direction: column;
    align-items: center;
    justify-content: center;
    gap: 70px;
  }
  .direction-text {
    font-family: "Oswald", sans-serif;
    font-weight: 700;
    font-size: 150px;
    line-height: 1.08;
    color: var(--sign-white);
    text-align: center;
    text-transform: uppercase;
    margin: 0;
  }
  .direction-arrow {
    width: 280px;
    height: 150px;
    display: block;
  }
</style>
</head>
<body>
<main class="canvas">

  <section class="sign-face sign-right" aria-label="Office entrance sign, arrow pointing right">
    <header class="brand-header">
      <span class="brand-mark"></span>
      <span class="brand-name">skorNABEL</span>
    </header>
    <div class="direction-panel">
      <div class="panel-frame">
        <h1 class="direction-text">Office<br>Entrance</h1>
        <svg class="direction-arrow" viewBox="0 0 280 150" aria-hidden="true">
          <rect x="0" y="0" width="280" height="150" rx="14" fill="#ffffff"/>
          <polygon points="40,58 160,58 160,22 240,75 160,128 160,92 40,92" fill="#2452a8"/>
        </svg>
      </div>
    </div>
  </section>

  <section class="sign-face sign-left" aria-label="Office entrance sign, arrow pointing left">
    <header class="brand-header">
      <span class="brand-mark"></span>
      <span class="brand-name">skorNABEL</span>
    </header>
    <div class="direction-panel">
      <div class="panel-frame">
        <h1 class="direction-text">Office<br>Entrance</h1>
        <svg class="direction-arrow" viewBox="0 0 280 150" aria-hidden="true">
          <rect x="0" y="0" width="280" height="150" rx="14" fill="#ffffff"/>
          <polygon points="240,58 120,58 120,22 40,75 120,128 120,92 240,92" fill="#2452a8"/>
        </svg>
      </div>
    </div>
  </section>

</main>
</body>
</html>
```